Advertisement flyer for fire sprinkler repair parts. The projected audience are contractors.

I need a flyer advertising specific parts that we are stocking at our company "Northgate Valve Supply." I have attached a picture of our logo. I want the title to say "Fire Pump Repair Parts and Accessories." I want to specifically advertise the following parts: Repack Kits and Repair Parts, Jockey Pumps, Pump Controllers, Casing Relief Valves, Air Release Valves, Suction/Discharge Gauges, Pump Shaft Couplers & Shim Kits, Fire Pump Relief Valves, and UL Listed Pressure Reducing Valves. I have attached pictures of the manufacturers I want to advertise on this flyer. I have also attached pictures of some of the parts we are stocking that I would like to be included somewhere in the flyer. I would like all of the pictures to have a transparent background. Also I would like our phone number :(800)-482-3067, and our website www.ridgeflowsupply.com included. I made my own design that I have Attached. You do not have to go based off this design, but I would like the basic content to be the same. We do have Same- Day shipping as well as Free Tech Support if you can include that anywhere.

```html
<!DOCTYPE html>
<html lang="en">
<head>
<meta charset="utf-8">
<title>Fire Pump Repair Parts &amp; Accessories — Northgate Valve Supply</title>
<link rel="stylesheet" href="https://fonts.googleapis.com/css2?family=Alegreya+Sans+SC:wght@800&family=Oswald:wght@500;600&family=Arvo:wght@400;700&family=Arimo:wght@700&display=swap">
<style>
  :root{
    --backdrop:#3b3b3b;
    --red:#c0161f;
    --red-dark:#9e0f17;
    --red-light:#d8434a;
    --white:#ffffff;
    --ink:#1c1c1c;
    --navy:#2b3f8f;
    --steel-1:#dcdcdc;
    --steel-2:#8b8b8b;
  }
  *{box-sizing:border-box;margin:0;padding:0}
  html,body{width:1080px;height:1200px;overflow:hidden;background:var(--backdrop)}
  .flyer{position:absolute;left:115px;top:0;width:850px;height:1200px;background:var(--white);overflow:hidden}

  .header{position:absolute;left:0;top:0;width:850px;height:231px;
    background:linear-gradient(100deg,var(--red-dark) 0%,var(--red-light) 45%,var(--red) 100%);
    display:flex;align-items:center;justify-content:center;text-align:center}
  .title{font-family:"Alegreya Sans SC",sans-serif;font-weight:800;color:var(--white);
    font-size:66px;line-height:1.0;letter-spacing:1px}

  .hero{position:absolute;left:0;top:231px;width:850px;height:518px;
    background:linear-gradient(160deg,#e9e9e9 0%,#a9a9a9 35%,#6e6e6e 70%,#9a9a9a 100%)}
  .product-shots{position:absolute;left:40px;top:80px;width:275px;height:348px;
    background:linear-gradient(180deg,#f2f2f2,#d5d5d5)}

  .parts-list{position:absolute;left:344px;top:78px;list-style:none}
  .parts-list li{position:relative;padding-left:34px;height:44px;
    font-family:"Oswald",sans-serif;font-weight:600;font-size:28px;line-height:44px;color:var(--red);
    text-shadow:2px 0 0 #fff,-2px 0 0 #fff,0 2px 0 #fff,0 -2px 0 #fff,2px 2px 0 #fff,-2px -2px 0 #fff,2px -2px 0 #fff,-2px 2px 0 #fff,3px 3px 4px rgba(0,0,0,.5);
    white-space:nowrap}
  .parts-list li::before{content:"";position:absolute;left:4px;top:15px;width:14px;height:14px;border-radius:50%;
    background:var(--red);border:3px solid var(--white)}

  .brand-panel{position:absolute;left:38px;top:790px;width:776px;height:245px;
    border:3px solid var(--red);border-radius:14px;overflow:hidden;background:var(--white)}
  .service{position:absolute;left:0;top:0;width:257px;height:100%;background:var(--red);
    color:var(--white);text-align:center}
  .service-icons{position:absolute;left:40px;top:26px}
  .service-text{position:absolute;left:0;right:0;top:118px;font-family:"Arvo",serif;font-size:22px;line-height:27px}
  .social{position:absolute;left:0;right:0;top:184px;display:flex;justify-content:center;gap:6px}
  .social span{width:20px;height:20px;border-radius:50%;background:var(--white)}

  .makers{position:absolute;left:257px;top:0;right:0;height:100%;padding:22px 18px}
  .maker-row{display:flex;justify-content:space-around;align-items:center;height:58px}
  .maker{font-family:"Arimo",sans-serif;font-weight:700;font-size:16px;color:var(--navy);white-space:nowrap;display:flex;align-items:center;gap:6px}
  .maker.red{color:var(--red)}
  .maker .dot{width:12px;height:12px;background:currentColor}
  .maker.lead{font-size:34px;color:var(--navy);gap:14px;margin-top:8px;justify-content:center}
  .maker.lead .dot{width:42px;height:42px;background:var(--red);border-radius:50%}

  .call{position:absolute;left:0;right:0;top:1065px;text-align:center;
    font-family:"Arvo",serif;font-size:46px;color:var(--red);white-space:nowrap}
  .call strong{font-weight:700}
  .web{position:absolute;left:0;right:0;top:1125px;text-align:center;
    font-family:"Arvo",serif;font-size:32px;letter-spacing:9px;color:var(--ink)}
</style>
</head>
<body>
<main class="flyer">
  <header class="header">
    <h1 class="title">Fire Pump Repair<br>Parts &amp; Accessories</h1>
  </header>

  <section class="hero" role="img" aria-label="Photo of a fire pump room with piping and equipment">
    <div class="product-shots" role="img" aria-label="Product photos: jockey pump, pressure reducing valve and red fire pumps"></div>
    <ul class="parts-list">
      <li>Repack Kits &amp; Repair Parts,</li>
      <li>Jockey Pumps,</li>
      <li>Pump Controllers,</li>
      <li>Casing Relief Valves,</li>
      <li>Air Release Valves,</li>
      <li>Suction/Discharge Gauges,</li>
      <li>Pump Shaft Couplers &amp; Shim Kits</li>
      <li>Fire Pump Relief Valves</li>
      <li>&amp; UL Listed Pressure Reducing Valves.</li>
    </ul>
  </section>

  <section class="brand-panel">
    <div class="service">
      <svg class="service-icons" width="180" height="86" viewBox="0 0 180 86" aria-hidden="true">
        <path d="M70 18 A36 36 0 1 0 76 50" fill="none" stroke="#fff" stroke-width="4"/>
        <path d="M64 10 L74 20 L62 26" fill="none" stroke="#fff" stroke-width="4"/>
        <text x="40" y="46" text-anchor="middle" font-family="Arimo, sans-serif" font-weight="700" font-size="14" fill="#fff">SAME DAY</text>
        <text x="40" y="60" text-anchor="middle" font-family="Arimo, sans-serif" font-size="9" fill="#fff" letter-spacing="1">DELIVERY</text>
        <circle cx="138" cy="28" r="18" fill="#fff"/>
        <path d="M116 30 A22 22 0 0 1 160 30" fill="none" stroke="#fff" stroke-width="4"/>
        <rect x="112" y="26" width="8" height="14" rx="3" fill="#fff"/>
        <rect x="156" y="26" width="8" height="14" rx="3" fill="#fff"/>
        <path d="M110 86 Q112 52 138 52 Q164 52 166 86 Z" fill="#fff"/>
      </svg>
      <p class="service-text">Same- Day shipping<br>Free Tech Support</p>
      <div class="social" aria-label="Social media"><span></span><span></span><span></span><span></span><span></span></div>
    </div>
    <div class="makers">
      <div class="maker-row">
        <span class="maker red"><i class="dot"></i>Crestline Pumps</span>
        <span class="maker">Halvor Pumps</span>
        <span class="maker">Bramwell Pump</span>
        <span class="maker red">Tessor Valve</span>
      </div>
      <div class="maker-row">
        <span class="maker">Kinross Pump</span>
        <span class="maker">Aldane Pumps</span>
        <span class="maker">Vantor</span>
        <span class="maker">Fenwick Marsh</span>
      </div>
      <div class="maker-row">
        <span class="maker lead"><i class="dot"></i>Northgate Valve Supply</span>
      </div>
    </div>
  </section>

  <p class="call">CALL US TODAY: <strong>(800)-482-3067</strong></p>
  <p class="web">WWW.RIDGEFLOWSUPPLY.COM</p>
</main>
</body>
</html>
```